Business Card Design needed Have Logo Files

Hello, I am in need of a business card design.

Company Name: Quartz Traders

Company Address:
2714 E. Palmer Ave
Suite 482B
North Las Vegas, Nevada 97415

I think the colors blue, grey, silver (metallic), white, and black are good choices to go with for coloring.

The Owen Pratt and the Copper Sheet are my favorites from the examples so far. Love the bring and edgy blues.

Photo's I have added are designs that I like. I'll also be adding source files.

Logo Source documents have been added.

Project Deadline Extended
Reason: Father passed away and had to take care of his affairs, back in business now.

Need front and back. Try to give it a backside that has a wow factor to it. I've changed the color spectrum to blue, black, purple, and pink for the front side. Think of it as 90% blue and black, 7% purple, 3 % pink when it comes to thinking of ratios of how much of each color i'd like to see on the card. Backside you can use any of those 4 colors as much as you'd like to give it memorable.

Industry/Entity Type

Business

Colors
0492cd
33a6d7
0355a3
3176b5
ffffff
aaaaaa
cbcbcb
9d9d9d
5c5c5c

Requirements
Must have
• Name
Company Address
Work Number
Mobile Number

Doublesided.
Rounded edges

```html
<!DOCTYPE html>
<html lang="en">
<head>
<meta charset="utf-8">
<title>Quartz Traders – Business Card</title>
<link rel="stylesheet" href="https://fonts.googleapis.com/css2?family=Arimo:wght@400;700&display=swap">
<style>
  :root {
    --stage: #1b1b1b;
    --card-black: #000000;
    --brand-blue: #1fa8e8;
    --text-blue: #33a6d7;
    --deep-blue: #0355a3;
    --mid-blue: #0492cd;
    --light-blue: #5cc8f5;
    --accent-purple: #7a3fc8;
    --accent-pink: #e04fb0;
  }
  * { margin: 0; padding: 0; box-sizing: border-box; }
  html, body {
    width: 1200px;
    height: 1000px;
    overflow: hidden;
    background: var(--stage);
    font-family: "Arimo", Arial, sans-serif;
  }
  .canvas {
    position: relative;
    width: 1200px;
    height: 1000px;
  }
  .card {
    position: absolute;
    top: 342px;
    width: 540px;
    height: 317px;
    border-radius: 20px;
    background: var(--card-black);
    overflow: hidden;
  }
  .card--front { left: 40px; }
  .card--back { left: 620px; }

  .card__art {
    position: absolute;
    inset: 0;
    width: 100%;
    height: 100%;
  }

  .wordmark {
    display: flex;
    align-items: center;
    gap: 10px;
    color: var(--brand-blue);
    font-weight: 700;
    letter-spacing: 0.04em;
    text-transform: uppercase;
  }
  .wordmark__dot {
    border-radius: 50%;
    background: var(--brand-blue);
    flex: none;
  }

  .card--front .wordmark {
    position: absolute;
    left: 24px;
    top: 34px;
    font-size: 30px;
  }
  .card--front .wordmark__dot { width: 24px; height: 24px; }

  .contact {
    position: absolute;
    left: 35px;
    top: 96px;
    color: var(--text-blue);
    font-size: 15px;
    line-height: 20px;
    font-style: normal;
  }
  .contact__group + .contact__group { margin-top: 9px; }

  .card--back .wordmark {
    position: absolute;
    left: 50%;
    top: 50%;
    transform: translate(-50%, -50%);
    font-size: 58px;
    gap: 16px;
  }
  .card--back .wordmark__dot { width: 46px; height: 46px; }
</style>
</head>
<body>
<main class="canvas">

  <section class="card card--front" aria-label="Business card front">
    <svg class="card__art" viewBox="0 0 370 217" preserveAspectRatio="none">
      <defs>
        <linearGradient id="smokeGradient" x1="1" y1="0" x2="0.3" y2="1">
          <stop offset="0" stop-color="#5cc8f5"/>
          <stop offset="0.4" stop-color="#0492cd"/>
          <stop offset="0.75" stop-color="#0355a3"/>
          <stop offset="0.92" stop-color="#7a3fc8"/>
          <stop offset="1" stop-color="#e04fb0"/>
        </linearGradient>
      </defs>
      <path role="img" aria-label="Blue smoke swirl artwork with violet and pink glow"
            d="M314 0 H370 V217 H235 C290 170 330 110 330 60 C330 35 325 15 314 0 Z"
            fill="url(#smokeGradient)"/>
      <path d="M318 38 C330 80 320 140 285 190" fill="none" stroke="#000" stroke-width="3"/>
      <path d="M345 120 C345 160 325 195 300 217" fill="none" stroke="#e04fb0" stroke-width="1.2" opacity="0.8"/>
    </svg>

    <div class="wordmark">
      <span class="wordmark__dot"></span>
      <span class="wordmark__name">Quartz</span>
    </div>

    <address class="contact">
      <div class="contact__group">
        <p>Owen Pratt</p>
        <p>Quartz Traders</p>
      </div>
      <div class="contact__group">
        <p>Address:</p>
        <p>2714 E. Palmer Ave</p>
        <p>Suite 482B</p>
        <p>North Las Vegas, Nevada 97415</p>
      </div>
      <div class="contact__group">
        <p>Work: (702) 555-0148</p>
        <p>Mobile: (702) 555-0193</p>
      </div>
    </address>
  </section>

  <section class="card card--back" aria-label="Business card back">
    <div class="wordmark">
      <span class="wordmark__dot"></span>
      <span class="wordmark__name">Quartz</span>
    </div>
  </section>

</main>
</body>
</html>
```